Red Gum Business Card Design

We are a new small business specialising in under ground cable jointing and excavation works in NSW Australia.
Design I'm looking for is incorporating the Australian flag & excavator with out being to cheesy.
Maybe a faded washed out flag to help with overload of colour? & so its not the main focus.
Very open to creative out of the box designs!

Target Market(s)

Building & Construction

Industry/Entity Type

Construction

Contact Information for Business Card

Red Gum Cable Jointing & Excavations
Owen Falkirk

Ph: 0438 605 312
E: owen.falkirk@tallmail.example

Reverse Side
Services we offer:
High Voltage & Low Voltage Cable Jointing
Polymeric & paperlead jointing & terminations
Trenching & Auger Drilling 150 - 600mm
Site preparation / leveling / clearing
Driveway / Footpath / Turf Prep
Rubbish Removal
Tree & Stump removal
Footings & Post holes
Drainage
Service Installs
Gravels & Sands available
Any general Earth moving needs
Reliable Free Quotes
Fully Insured

Font styles to use
Serif
Script

Requirements
Nice to have
• small excavator (See uploaded picture)

```html
<!DOCTYPE html>
<html lang="en">
<head>
<meta charset="utf-8">
<title>Red Gum Business Card Design</title>
<link rel="stylesheet" href="https://fonts.googleapis.com/css2?family=Varela+Round&family=Open+Sans:wght@400;600;700&display=swap">
<style>
  :root {
    --navy: #1d4f9c;
    --navy-deep: #143d80;
    --red: #e01f2d;
    --white: #ffffff;
    --paper: #f4f5f7;
    --grey: #6b6f76;
    --backdrop: #d9d4cc;
  }
  * { margin: 0; padding: 0; box-sizing: border-box; }
  html, body { width: 1200px; height: 1023px; overflow: hidden; }
  body { background: var(--backdrop); position: relative; font-family: "Open Sans", sans-serif; }

  .card {
    position: absolute;
    width: 560px;
    height: 342px;
    border-radius: 4px;
    overflow: hidden;
    box-shadow: 0 10px 28px rgba(0,0,0,0.25);
  }
  .card-art { position: absolute; inset: 0; width: 100%; height: 100%; }

  /* Front */
  .card-front { left: 60px; top: 110px; background: var(--paper); }
  .brand-mark {
    position: absolute; left: 26px; top: 150px;
    display: flex; align-items: center; gap: 8px;
    font-family: "Varela Round", sans-serif; font-size: 14px; color: var(--navy);
  }
  .brand-mark .dot { width: 14px; height: 14px; border-radius: 50%; background: var(--navy); }
  .company-name {
    position: absolute; left: 130px; top: 34px; width: 380px;
    font-family: "Varela Round", sans-serif; font-weight: 400; font-size: 29px; line-height: 1.12;
    color: var(--navy);
  }
  .person { position: absolute; left: 130px; top: 122px; }
  .person-name { font-family: "Varela Round", sans-serif; font-size: 22px; color: var(--navy); }
  .person-role { font-size: 12px; color: var(--grey); margin-top: 1px; }
  .contact { position: absolute; left: 130px; top: 176px; font-size: 12px; color: var(--grey); }
  .contact li { list-style: none; display: flex; align-items: center; gap: 8px; margin-bottom: 3px; }
  .contact svg { width: 11px; height: 11px; fill: var(--navy); }

  /* Back */
  .card-back { left: 580px; top: 540px; background: var(--white); }
  .services { position: absolute; left: 28px; top: 14px; color: var(--white); font-size: 12px; line-height: 1.17; }
  .services-title { font-weight: 700; }
  .services li { list-style: none; }
  .back-mark {
    position: absolute; right: 40px; bottom: 12px;
    display: flex; align-items: center; gap: 10px;
    font-family: "Varela Round", sans-serif; font-size: 26px; color: var(--navy);
  }
  .back-mark .dot { width: 26px; height: 26px; border-radius: 50%; background: var(--navy); }
</style>
</head>
<body>

<section class="card card-front">
  <svg class="card-art" viewBox="0 0 560 342" preserveAspectRatio="none" aria-hidden="true">
    <path d="M0 312 C330 302 520 227 560 -3 L560 342 L0 342 Z" fill="var(--red)"/>
    <path d="M0 320 C330 310 520 235 560 5 L560 342 L0 342 Z" fill="var(--white)"/>
    <path d="M0 328 C330 318 520 243 560 13 L560 342 L0 342 Z" fill="var(--navy)"/>
  </svg>
  <div class="brand-mark"><span class="dot"></span>Red Gum</div>
  <h1 class="company-name">Red Gum Cable<br>Jointing &amp; Excavations</h1>
  <div class="person">
    <div class="person-name">Owen Falkirk</div>
    <div class="person-role">Director</div>
  </div>
  <ul class="contact">
    <li><svg viewBox="0 0 24 24"><path d="M6.6 10.8a15.1 15.1 0 0 0 6.6 6.6l2.2-2.2c.3-.3.7-.4 1-.2 1.1.4 2.3.6 3.6.6.6 0 1 .4 1 1V20c0 .6-.4 1-1 1A17 17 0 0 1 3 4c0-.6.4-1 1-1h3.5c.6 0 1 .4 1 1 0 1.3.2 2.5.6 3.6.1.3 0 .7-.2 1z"/></svg>0438 605 312</li>
    <li><svg viewBox="0 0 24 24"><path d="M2 5h20v14H2zM4 7v.5l8 5 8-5V7l-8 5z"/></svg>owen.falkirk@tallmail.example</li>
  </ul>
</section>

<section class="card card-back">
  <svg class="card-art" viewBox="0 0 560 342" preserveAspectRatio="none" aria-hidden="true">
    <path d="M0 0 H560 V290 C400 252 150 240 0 250 L0 0 Z" fill="var(--red)"/>
    <path d="M0 0 H560 V280 C400 242 150 230 0 240 L0 0 Z" fill="var(--navy)"/>
  </svg>
  <div class="services">
    <div class="services-title">Services We Offer:</div>
    <ul>
      <li>High Voltage &amp; Low Voltage Cable Jointing</li>
      <li>Polymeric &amp; Paperlead Jointing &amp; Terminations</li>
      <li>Trenching &amp; Auger Drilling 150 - 600mm</li>
      <li>Site Preparation / Leveling / Clearing</li>
      <li>Driveway / Footpath / Turf Prep</li>
      <li>Rubbish Removal</li>
      <li>Tree &amp; Stump Removal</li>
      <li>Footings &amp; Post Holes</li>
      <li>Drainage</li>
      <li>Service Installs</li>
      <li>Gravels &amp; Sands Available</li>
      <li>Any General Earth Moving Needs</li>
      <li>Reliable Free Quotes</li>
      <li>Fully Insured</li>
    </ul>
  </div>
  <div class="back-mark"><span class="dot"></span>Red Gum</div>
</section>

</body>
</html>
```